High End Art Gallery Business Card

We're looking for a business card design that is elegant and artful. Foil embossing, blind embossed pattern, or some kind of "extra" element to make it stand out. Standard American size. The back should remain blank or nearly blank so that notes can be written on the back.
Please check our website at kestrelvane.com to see information about our gallery and the type of artwork that we sell.
Included with the files is a brand identity guideline. In addition to the colors listed, we like to incorporate an indigo blue. The business card design in the guideline seems too simplistic. I have included some photos of other business card designs that have caught my eye.
thank you!

Contact Information for Business Card

Marisol Tevard
Gallery Owner
remaining details are in the attached docs

• some kind of natural/organic element to reflect the hand-made nature of all of the original artwork.

```html
<!DOCTYPE html>
<html lang="en">
<head>
<meta charset="utf-8">
<title>Kestrel Vane Gallery — Business Card</title>
<link rel="stylesheet" href="https://fonts.googleapis.com/css2?family=Open+Sans:wght@400;600&display=swap">
<style>
  :root {
    --stage: #161616;
    --card-white: #fbfbfa;
    --marble-vein: #d9d9d7;
    --marble-cloud: #ececea;
    --ink: #2f2f2f;
    --ink-soft: #4a4a4a;
    --gold-light: #f7d84a;
    --gold-mid: #e2b321;
    --gold-deep: #b8860f;
    --logo-gold: #ad8b52;
  }
  * { box-sizing: border-box; }
  html, body {
    margin: 0;
    width: 1200px;
    height: 1200px;
    overflow: hidden;
    background: var(--stage);
    font-family: "Open Sans", sans-serif;
  }
  .stage {
    position: relative;
    width: 1200px;
    height: 1200px;
  }
  .card {
    position: absolute;
    left: 160px;
    width: 880px;
    height: 503px;
    background: var(--card-white);
    overflow: hidden;
    box-shadow: 0 12px 30px rgba(0,0,0,0.55);
  }
  .card--back { top: 70px; }
  .card--front { top: 627px; }

  .marble {
    position: absolute;
    inset: 0;
    background:
      radial-gradient(ellipse 40% 18% at 25% 10%, var(--marble-cloud), transparent 70%),
      radial-gradient(ellipse 30% 50% at 88% 60%, var(--marble-cloud), transparent 70%),
      radial-gradient(ellipse 35% 20% at 15% 65%, var(--marble-cloud), transparent 70%),
      linear-gradient(155deg, var(--card-white) 0%, #f3f3f2 45%, var(--card-white) 100%);
  }

  .foil {
    position: absolute;
    inset: 0;
    width: 100%;
    height: 100%;
  }

  .brand {
    position: absolute;
    display: flex;
    align-items: center;
  }
  .brand__disc {
    border-radius: 50%;
    background: var(--logo-gold);
    flex: none;
  }
  .brand__name {
    color: var(--ink);
    font-weight: 400;
    text-transform: uppercase;
    white-space: nowrap;
  }

  .card--back .brand { top: 40px; right: 42px; }
  .card--back .brand__disc { width: 62px; height: 62px; margin-right: 16px; }
  .card--back .brand__name { font-size: 15px; letter-spacing: 2.5px; }

  .card--front .brand { top: 150px; left: 190px; }
  .card--front .brand__disc { width: 150px; height: 150px; margin-right: 34px; }
  .card--front .brand__name { font-size: 32px; letter-spacing: 4px; }

  .contact-row {
    position: absolute;
    left: 70px;
    right: 60px;
    bottom: 58px;
    display: flex;
    align-items: baseline;
    color: var(--ink-soft);
    white-space: nowrap;
  }
  .contact-row__name {
    font-size: 32px;
    font-weight: 600;
    color: var(--ink);
  }
  .contact-row__sep {
    font-size: 18px;
    margin: 0 10px;
  }
  .contact-row__role { font-size: 18px; }
  .contact-row__phone { font-size: 20px; margin-left: 34px; }
  .contact-row__email { font-size: 20px; }

  .gold-rule {
    position: absolute;
    left: 0;
    right: 0;
    bottom: 36px;
    height: 4px;
    background: linear-gradient(90deg, var(--gold-mid), var(--gold-light), var(--gold-mid));
  }
</style>
</head>
<body>
<main class="stage">

  <section class="card card--back" aria-label="Card back">
    <div class="marble" role="img" aria-label="White Carrara marble texture with soft grey veining"></div>
    <svg class="foil" viewBox="0 0 880 503" preserveAspectRatio="none" aria-hidden="true">
      <defs>
        <linearGradient id="foilGold" x1="0" y1="0" x2="1" y2="1">
          <stop offset="0" stop-color="var(--gold-deep)"/>
          <stop offset="0.45" stop-color="var(--gold-light)"/>
          <stop offset="1" stop-color="var(--gold-mid)"/>
        </linearGradient>
      </defs>
      <path d="M0 0 H430 C405 12 380 10 350 22 C300 30 240 38 190 55 C140 72 110 88 70 100 C40 112 20 120 0 130 Z" fill="url(#foilGold)"/>
      <path d="M880 330 C855 345 835 360 820 385 C800 410 770 425 735 445 C700 465 660 480 610 503 H880 Z" fill="url(#foilGold)"/>
    </svg>
    <div class="brand">
      <span class="brand__disc" aria-hidden="true"></span>
      <span class="brand__name">Kestrel Vane Gallery</span>
    </div>
  </section>

  <section class="card card--front" aria-label="Card front">
    <div class="marble" role="img" aria-label="White Carrara marble texture with soft grey veining"></div>
    <div class="brand">
      <span class="brand__disc" aria-hidden="true"></span>
      <span class="brand__name">Kestrel Vane Gallery</span>
    </div>
    <div class="contact-row">
      <span class="contact-row__name">Marisol Tevard</span>
      <span class="contact-row__sep">/</span>
      <span class="contact-row__role">Gallery Owner</span>
      <span class="contact-row__phone">0312-55810-276</span>
      <span class="contact-row__sep">/</span>
      <span class="contact-row__email">info@kestrelvane.com</span>
    </div>
    <div class="gold-rule" aria-hidden="true"></div>
  </section>

</main>
</body>
</html>
```